TIKLOOMTOT WEBSITE DESIGN

We need a website design based on the template- http://varolapixels.com/themes/quartzpage-bootstrap-wordpress-theme/. We purchased template and will build the website using wordpress. It is one page application. We wanted to list all content in one page and make it browser friendly (can be viewed in cell phone, pc, mac, ipad, etc).

The target audience is parents with babies/kids age from 0-5 year old. We wanted to sell the subscription based monthly boxes to the families. The box will include books, toys, crafts, kids consumer products and letter/note/card to the family from the experts. All boxes are customized based on children's age, gender and interests.

We wanted the site main color to be blue.

Please refer to these websites for ideas.
froxi.com
wwws.pebbleharbor.com
http://www.wigglyoats.com/

I've updated the project brief and make the project fund guaranteed. Thanks!

Target Market(s)

Parents with kids age from 0-5 years old. Mainly target to the China market.

Industry/Entity Type

Cell Phone

Colors
3277b5
85abd2
85cae6
33a6d7
0592cd
0355a3
ceddec
cee9f5

Requirements
Must have
• Must provide the design based on the template- http://varolapixels.com/themes/quartzpage-bootstrap-wordpress-theme/.
The site has to be Chinese character friendly since we are going to post Chinese content on the website. No English content.
The registration forms needs to be designed and include in the final deliverable.

```html
<!DOCTYPE html>
<html lang="en">
<head>
<meta charset="utf-8">
<title>TIKLOOMTOT</title>
<link href="https://fonts.googleapis.com/css2?family=Raleway:wght@400;500;600;700;800&display=swap" rel="stylesheet">
<style>
:root{
  --navy:#0355a3;
  --navy-deep:#02468a;
  --sky:#33a6d7;
  --sky-light:#5bbbe3;
  --azure:#0592cd;
  --pale:#cee9f5;
  --ink:#222a33;
  --muted:#4a4f57;
  --btn-dark:#3a3f47;
  --footer:#3d4452;
  --red:#e02a1c;
  --white:#ffffff;
}
*{box-sizing:border-box;margin:0;padding:0}
html,body{width:1200px;height:2573px;overflow:hidden}
body{font-family:'Raleway',sans-serif;color:var(--ink);background:var(--white);position:relative}
.abs{position:absolute}

/* header */
.site-header{position:absolute;left:0;top:0;width:1200px;height:105px;background:linear-gradient(180deg,var(--navy) 0%,var(--navy-deep) 100%)}
.brand{position:absolute;left:107px;top:26px;display:flex;align-items:center;gap:12px}
.brand-dot{width:54px;height:54px;border-radius:50%;background:var(--white)}
.brand-name{color:var(--white);font-weight:800;font-size:16px;letter-spacing:.3px}
.main-nav{position:absolute;left:570px;top:49px;display:flex;align-items:center;font-size:10.5px;font-weight:700;color:var(--white);letter-spacing:.3px}
.main-nav span.sep{margin:0 9px;opacity:.9}
.main-nav .active{color:var(--pale)}
.caret{display:inline-block;margin-left:5px;border-left:4px solid transparent;border-right:4px solid transparent;border-top:4px solid var(--white);vertical-align:middle}
.chat-link{position:absolute;left:1022px;top:30px;width:70px;height:50px}
.chat-link svg{position:absolute;left:18px;top:0}
.chat-link b{position:absolute;left:2px;top:20px;font-size:10.5px;font-weight:800;color:var(--white)}

/* hero */
.hero{position:absolute;left:0;top:105px;width:1200px;height:617px;background:linear-gradient(180deg,var(--sky-light) 0%,var(--sky) 100%);color:var(--white);text-align:center}
.hero-kicker{position:absolute;left:0;width:1200px;top:44px;font-size:17px;font-weight:500;line-height:22px}
.hero-title{position:absolute;left:0;width:1200px;top:88px;font-size:35px;font-weight:600;line-height:42px}
.hero-copy{position:absolute;left:230px;width:740px;top:178px;font-size:12.3px;line-height:15.5px;font-weight:500}
.browser{position:absolute;left:132px;top:303px;width:936px;height:314px;background:#f1f2f4;border-radius:6px 6px 0 0;box-shadow:0 8px 22px rgba(0,40,90,.35);overflow:hidden}
.browser-bar{position:absolute;left:0;top:0;width:936px;height:66px;background:linear-gradient(180deg,#eef0f2,#dfe2e6)}
.dot{position:absolute;top:12px;width:10px;height:10px;border-radius:50%}
.tab{position:absolute;left:80px;top:8px;width:150px;height:20px;background:#f7f8f9;border-radius:5px 5px 0 0}
.url{position:absolute;left:74px;top:38px;width:820px;height:18px;background:var(--white);border:1px solid #c9ced4;border-radius:3px}
.browser-stripe{position:absolute;left:0;top:66px;width:936px;height:8px;background:#4a4f57}
.showcase{position:absolute;top:74px;height:240px}
.showcase.a{left:0;width:469px;background:linear-gradient(135deg,#c9b79a,#8fa3b8 55%,#e8e3d8)}
.showcase.b{left:469px;width:467px;background:linear-gradient(135deg,#b8401f,#e87a2a 45%,#c23a18)}

/* experts */
.experts{position:absolute;left:0;top:722px;width:1200px;height:454px;background:var(--white)}
.expert{position:absolute;top:92px;width:230px;text-align:center}
.avatar{width:104px;height:104px;border-radius:50%;margin:0 auto;background:linear-gradient(160deg,#e7d6c6,#9fa9b5);border:3px solid #f1f1f1}
.expert h3{margin-top:24px;font-size:14.3px;font-weight:700;color:var(--ink)}
.expert p{margin:7px auto 0;width:210px;font-size:9.8px;line-height:11.6px;color:var(--muted);font-weight:500;height:87px}
.btn{display:inline-block;font-weight:700;color:var(--white);border-radius:3px;text-align:center}
.btn-more{width:77px;height:28px;line-height:28px;font-size:10.5px;background:var(--btn-dark)}
.btn-more.blue{background:var(--sky)}

/* products */
.products-title{position:absolute;left:0;width:1200px;top:1216px;text-align:center;font-size:20px;font-weight:700;color:var(--ink)}
.products-band{position:absolute;left:0;top:1259px;width:1200px;height:345px;background:var(--navy)}
.tile{position:absolute;width:230px;height:172px}
.tile.t1{left:50px;top:0;background:linear-gradient(135deg,#b7c4d3,#8ea3bb 50%,#e2e0db)}
.tile.t2{left:280px;top:0;background:#2f6fb7}
.tile.t3{left:510px;top:0;background:linear-gradient(135deg,#f1c9d3,#d9c0c6 55%,#e9e6e2)}
.tile.t4{left:50px;top:172px;background:linear-gradient(135deg,#f3f3f5,#e9c25a 45%,#e35247)}
.tile.t5{left:280px;top:172px;background:linear-gradient(135deg,#c4442d,#9aa6b6 55%,#e2dccf)}
.tile.t6{left:510px;top:172px;background:linear-gradient(135deg,#f4f3f6,#7bb0d8 50%,#f4f3f6)}
.tile-caption{position:absolute;left:0;width:230px;top:52px;text-align:center;color:var(--white);font-size:12px;font-weight:700}
.tile-caption b{font-size:15px}
.tile-icons{position:absolute;top:90px;left:60px;display:flex;gap:26px}
.tile-icon{width:48px;height:30px;border:1.5px solid var(--white);border-radius:2px;display:flex;align-items:center;justify-content:center}
.order-panel{position:absolute;left:741px;top:0;width:459px;height:345px;background:linear-gradient(90deg,#0a5fb3,#0c63b9)}
.order-title{position:absolute;left:16px;top:26px;font-size:18px;font-weight:700;color:var(--white)}
.field{position:absolute;height:37px;background:var(--white);border-radius:2px;font-size:10.5px;color:#9aa0a7;padding:0 12px;line-height:37px;font-weight:500}
.field .caret{position:absolute;right:12px;top:16px;border-top-color:#555}
.plan{position:absolute;left:16px;top:250px;font-size:11px;font-weight:700;color:var(--white);display:flex;align-items:center}
.check{display:inline-block;width:15px;height:15px;background:var(--white);border-radius:2px;margin:0 10px 0 18px}
.btn-subscribe{position:absolute;left:16px;top:283px;width:393px;height:42px;line-height:42px;font-size:17px;font-weight:600;background:linear-gradient(180deg,#ee3a2a,var(--red));border-radius:3px;color:var(--white);text-align:center}

/* faq */
.faq{position:absolute;left:0;top:1604px;width:1200px;height:349px;background:var(--white)}
.faq h2{position:absolute;font-size:14.5px;font-weight:700;color:var(--ink)}
.rule{position:absolute;height:1.5px;background:var(--ink)}
.faq-intro{position:absolute;left:173px;top:104px;width:310px;font-size:9.9px;line-height:12.6px;color:var(--muted);font-weight:500}
.link-list{position:absolute;list-style:none;font-size:9.8px;font-weight:700;color:#1b5fa8;line-height:23.6px}
.faq .btn-more{position:absolute;left:173px;top:272px}

/* testimonial */
.testimonial{position:absolute;left:0;top:1953px;width:1200px;height:386px;background:linear-gradient(180deg,#8ec6e6 0%,#76b6df 60%,#86c2e2 100%);color:var(--white);text-align:center}
.quote-icon{position:absolute;left:553px;top:82px}
.quote-text{position:absolute;left:270px;width:660px;top:158px;font-size:12.8px;line-height:26px;font-weight:600}
.quote-name{position:absolute;left:0;width:1200px;top:266px;font-size:16px;font-weight:600;color:#f1f6fa}
.quote-role{position:absolute;left:0;width:1200px;top:290px;font-size:11px;font-weight:500;color:#eaf3f9}

/* footer */
.site-footer{position:absolute;left:0;top:2339px;width:1200px;height:234px;background:var(--footer);color:var(--white)}
.site-footer h4{position:absolute;top:53px;font-size:15px;font-weight:600}
.site-footer .rule{background:var(--white);top:83px}
.footer-menu{position:absolute;left:110px;top:96px;width:330px;font-size:9.6px;font-weight:700;line-height:20px}
.footer-menu .active{color:#5fc2ef}
.footer-menu .sep{margin:0 7px}
.socials{position:absolute;left:445px;top:115px;display:flex;gap:7px}
.social{width:44px;height:44px;border-radius:50%;border:2px solid var(--white)}
.contact{position:absolute;left:779px;top:96px;font-size:11.5px;line-height:20.5px;font-weight:500}
.contact b{font-weight:700}
</style>
</head>
<body>

<header class="site-header">
  <div class="brand"><span class="brand-dot"></span><span class="brand-name">TIKLOOMTOT</span></div>
  <nav class="main-nav">
    <span class="active">HOME</span><span class="sep">|</span>
    <span>ORDER NOW</span><span class="sep">|</span>
    <span>ABOUT US</span><span class="sep">|</span>
    <span>OUR EXPERTS</span><span class="sep">|</span>
    <span>FAQ</span><span class="sep">|</span>
    <span>SHARE<i class="caret"></i></span>
  </nav>
  <div class="chat-link">
    <svg width="50" height="42" viewBox="0 0 50 42"><path d="M25 3c11 0 20 7 20 16s-9 16-20 16c-3 0-5-.4-7-1l-8 6 2-8C8 29 5 24 5 19 5 10 14 3 25 3z" fill="none" stroke="#5fc2ef" stroke-width="2"/></svg>
    <b>CHATLINE</b>
  </div>
</header>

<section class="hero">
  <p class="hero-kicker">U.S. baby book club - let the children stay at home and enjoy the best the United States<br>early education and childcare philosophy platform.</p>
  <h1 class="hero-title">Subscribe now to our monthly mysterious<br>parcel,</h1>
  <p class="hero-copy">father and mother and baby can get U.S. experts recommend the award-winning children's books and American original reading experience, cultivate good habits of children daily necessities, as well as the latest toys handmade infant intellectual development. Mom and Dad will gain double surprise.<br>Authoritative parenting expert with the United States to exchange one pair of one, with the scientific, personalized parenting philosophy. Books and articles to help your baby healthy and happy growth.</p>
  <div class="browser">
    <div class="browser-bar">
      <span class="dot" style="left:12px;background:#e8574a"></span>
      <span class="dot" style="left:28px;background:#e9b53b"></span>
      <span class="dot" style="left:44px;background:#5cbf4a"></span>
      <span class="tab"></span>
      <svg class="abs" style="left:14px;top:40px" width="50" height="14" viewBox="0 0 50 14"><path d="M8 7h-6M5 4 2 7l3 3M14 7h6M17 4l3 3-3 3" stroke="#888" stroke-width="1.5" fill="none"/><path d="M32 7a4 4 0 1 1-1-3" stroke="#888" stroke-width="1.5" fill="none"/></svg>
      <span class="url"></span>
      <svg class="abs" style="left:906px;top:40px" width="14" height="14" viewBox="0 0 14 14"><path d="M2 3h10M2 7h10M2 11h10" stroke="#666" stroke-width="1.6"/></svg>
    </div>
    <div class="browser-stripe"></div>
    <div class="showcase a" role="img" aria-label="Open gift box with a plush teddy bear, crayons and picture books"></div>
    <div class="showcase b" role="img" aria-label="Red gift box with children's books, a sensory ball and a wooden toy"></div>
  </div>
</section>

<section class="experts">
  <div class="expert" style="left:89px">
    <div class="avatar" role="img" aria-label="Portrait of the pediatric expert"></div>
    <h3>Lin Haoran, MD, double</h3>
    <p>Bayview General Hospital pediatrician and physician Assistant clinical professor of pediatrics at Northgate Medical School National Pediatric Council (NPC) Senior Member Continental Pediatric Nutrition Society (CPNS) Member</p>
    <span class="btn btn-more">More info</span>
  </div>
  <div class="expert" style="left:346px">
    <div class="avatar" role="img" aria-label="Portrait of the pediatric dentistry expert"></div>
    <h3>Dr. Peter R. Dalton</h3>
    <p>A member of the National Pediatric Dental Society, Coastal Dental Guild members Eastshore Dental Society members Eastshore Institute of Pediatric Dentistry, former president</p>
    <span class="btn btn-more blue">More info</span>
  </div>
  <div class="expert" style="left:624px">
    <div class="avatar" role="img" aria-label="Portrait of the reading education expert"></div>
    <h3>Rosalind Whitcombe</h3>
    <p>American reading education experts Bachelor's degree from Alder University American English Master of Education, Lakeshore University renowned reading specialist certification</p>
    <span class="btn btn-more">More info</span>
  </div>
  <div class="expert" style="left:885px">
    <div class="avatar" role="img" aria-label="Portrait of the early childhood teacher"></div>
    <h3>Xiao Wen early childhood</h3>
    <p>New York, Riverside University Graduate School of Education Harborview private school teacher</p>
    <span class="btn btn-more">More info</span>
  </div>
</section>

<h2 class="products-title">PRODUCTS &amp; FORM</h2>
<section class="products-band">
  <div class="tile t1" role="img" aria-label="Blue teddy bear with crayons and a plate"></div>
  <div class="tile t2">
    <p class="tile-caption">PRODUCT NO: <b>2</b></p>
    <div class="tile-icons">
      <span class="tile-icon"><svg width="14" height="14" viewBox="0 0 14 14"><circle cx="6" cy="6" r="4" fill="none" stroke="#fff" stroke-width="1.6"/><path d="M9 9l4 4" stroke="#fff" stroke-width="1.6"/></svg></span>
      <span class="tile-icon"><svg width="14" height="14" viewBox="0 0 14 14"><path d="M6 8l2-2M5 6 3 8a2 2 0 0 0 3 3l2-2M9 8l2-2a2 2 0 0 0-3-3L6 5" fill="none" stroke="#fff" stroke-width="1.5"/></svg></span>
    </div>
  </div>
  <div class="tile t3" role="img" aria-label="Pink teddy bear with a plate"></div>
  <div class="tile t4" role="img" aria-label="Colourful wooden toy train"></div>
  <div class="tile t5" role="img" aria-label="Children's backpack with a plush toy and care products"></div>
  <div class="tile t6" role="img" aria-label="Wooden abacus counting frame"></div>

  <form class="order-panel">
    <h3 class="order-title">SUBSCRIBE MYSTERIOUS PARCEL</h3>
    <div class="field" style="left:16px;top:64px;width:193px">Child's Name</div>
    <div class="field" style="left:215px;top:64px;width:194px">Gender<i class="caret"></i></div>
    <div class="field" style="left:16px;top:107px;width:193px">Birth date (dd/mm/yy)</div>
    <div class="field" style="left:215px;top:107px;width:194px">Your email</div>
    <div class="field" style="left:16px;top:150px;width:393px">Mailing address</div>
    <div class="field" style="left:16px;top:193px;width:393px">Phone</div>
    <div class="plan">Select the subscription plan :<span class="check"></span>6 months<span class="check" style="margin-left:30px"></span>1 year</div>
    <div class="btn-subscribe">Subscribe now</div>
  </form>
</section>

<section class="faq">
  <h2 style="left:173px;top:63px">Frequently Asked Questions</h2>
  <div class="rule" style="left:173px;top:92px;width:612px"></div>
  <p class="faq-intro">We are parenting experts from the United States in New England, doctors, teachers and college professors, is a group dedicated to creating a better future moms and dads for children. In the daily work and life, we often see a lot of parents in the face of the child-related issues at a loss, and into errors in the direction of their children's education and methods. We voluntarily initiated TIKLOOMTOT, hope that through our many years of expertise and experience to provide you with school-age children the best educational programs as well as medical advice.</p>
  <ul class="link-list" style="left:496px;top:98px">
    <li>· How to join TIKLOOMTOT?</li>
    <li>· When will I receive my first one mysterious parcel?</li>
    <li>· Do I need to pay for shipping it?</li>
    <li>· I can send TIKLOOMTOT mysterious parcel to my friend?</li>
    <li>· About unsubscribe, you have what provisions?</li>
    <li>· What is your return policy is how to provide?</li>
  </ul>
  <span class="btn btn-more">More info</span>

  <h2 style="left:796px;top:63px">BLOG POSTS</h2>
  <div class="rule" style="left:796px;top:92px;width:229px"></div>
  <ul class="link-list" style="left:796px;top:98px">
    <li>What - TIKLOOMTOT is?</li>
    <li>When will I receive my mysterious parcel?</li>
    <li>How to join TIKLOOMTOT?</li>
    <li>Do I need to pay for shipping it?</li>
    <li>What is your return policy is how to provide?</li>
    <li>About unsubscribe, you have what provisions?</li>
  </ul>
</section>

<section class="testimonial" role="img" aria-label="Pale blue city skyline behind a client quote">
  <svg class="quote-icon" width="94" height="66" viewBox="0 0 94 66"><path d="M34 3c17 0 31 10 31 23S51 49 34 49c-3 0-6 0-9-1L11 58l4-14C8 40 3 33 3 26 3 13 17 3 34 3z" fill="#fff"/><path d="M66 22c14 0 25 9 25 19 0 6-3 11-8 14l3 10-11-7c-3 1-6 1-9 1-9 0-17-3-21-8 15-2 26-12 26-24z" fill="#fff"/></svg>
  <p class="quote-text">Lorem Ipsum is simply dummy text of the printing and typesetting industry. Lorem Ipsum has been the industry's standard dummy text ever since the 1500s, when an unknown printer took a galley of type and scrambled it to make a type specimen book. It has survived not only five centuries, but also the leap into electronic typesetting, remaining essentially unchanged.</p>
  <p class="quote-name">Edwin Callahan</p>
  <p class="quote-role">Managing director</p>
</section>

<footer class="site-footer">
  <h4 style="left:110px">MENU</h4>
  <div class="rule" style="left:110px;width:310px"></div>
  <p class="footer-menu"><span class="active">HOME</span><span class="sep">|</span>ORDER NOW<span class="sep">|</span>ABOUT US<span class="sep">|</span>OUR EXPERTS<br><span class="sep" style="margin-left:0">|</span>FAQ<span class="sep">|</span>SHARE<span class="sep">|</span>SITEMAP<span class="sep">|</span>PRIVACY POLICY</p>

  <h4 style="left:445px">Social Media</h4>
  <div class="rule" style="left:445px;width:310px"></div>
  <div class="socials">
    <span class="social" style="background:#3b5a9a"></span>
    <span class="social" style="background:#2aa9e0"></span>
    <span class="social" style="background:#8a5a3c"></span>
    <span class="social" style="background:#e0508a"></span>
    <span class="social" style="background:#16b08a"></span>
    <span class="social" style="background:#5a6470"></span>
  </div>

  <h4 style="left:779px">Contact Us</h4>
  <div class="rule" style="left:779px;width:310px"></div>
  <p class="contact">Maple Ave, 412, 10452, Lakeside,<br>United States.<br><b>Tlf.: + (155) 01 23 45 67 89</b><br><b>Mail: info@tikloomtot.com</b></p>
</footer>

</body>
</html>
```